Business card design for upmarket Home Technology design and Installation company

Hello designers, we need a great business card designed.
We need it to convey high tech, and also sophistication .
We work with some of the most affluent people in the world building them home technology systems, and A/V entertainment systems.

Services offered include the following:
Design, sales, installation, and maintenance of

*Home Automation systems
*Distributed / Multi-Room Audio and Video
*High Performance Networks & WiFi
* Lighting and Shade Control
*Home cinema
*Security and CCTV Systems

I have included a copy of our logo to use for your design efforts.

Target Market(s)

Upmarket clients with multi million euro villas.

Industry/Entity Type

Home technology

Contact Information for Business Card

NAME: Derek Halloran ADDRESS: Plaza Brisa Local 42, Port Andratx, 07392 PHONE: +34-602-518-794 EMAIL: DHalloran@VELTRAsmarthomes.com WEB: www.veltrasmarthomes.com

Requirements
Must have
• Our Logo, and our tagline

```html
<!DOCTYPE html>
<html lang="en">
<head>
<meta charset="utf-8">
<title>VELTRA Smarter Homes – Business Card</title>
<link rel="stylesheet" href="https://fonts.googleapis.com/css2?family=Lato:wght@400;700&family=Montserrat:wght@400&display=swap">
<style>
  :root {
    --page-bg: #e9e4dd;
    --card-dark: #1f1c1b;
    --card-mid: #2e2a28;
    --gold: #c89a45;
    --gold-light: #e2bb6a;
    --gold-deep: #a8782c;
    --text-soft: #d9d3cc;
  }
  * { margin: 0; padding: 0; box-sizing: border-box; }
  html, body {
    width: 1200px; height: 1047px; overflow: hidden;
    background: var(--page-bg);
  }
  .card {
    position: absolute; left: 80px; top: 240px;
    width: 1040px; height: 568px;
    border-radius: 26px;
    background: linear-gradient(180deg, var(--card-mid) 0%, var(--card-dark) 100%);
    box-shadow: 0 18px 40px rgba(0,0,0,0.25);
    overflow: hidden;
  }
  .brand-name {
    position: absolute; left: 0; right: 0; top: 48px;
    text-align: center;
    font-family: "Lato", sans-serif; font-weight: 700;
    font-size: 150px; letter-spacing: 18px; line-height: 1;
    color: var(--gold);
  }
  .tagline {
    position: absolute; left: 0; right: 0; top: 212px;
    text-align: center;
    font-family: "Lato", sans-serif; font-weight: 700;
    font-size: 44px; color: var(--gold);
  }
  .person {
    position: absolute; right: 552px; top: 312px; text-align: right;
    font-family: "Lato", sans-serif;
  }
  .person-name { font-size: 36px; font-weight: 700; color: var(--gold); }
  .person-role { font-size: 24px; color: var(--text-soft); margin-top: 10px; }
  .divider {
    position: absolute; left: 522px; top: 300px;
    width: 2px; height: 106px; background: var(--gold);
  }
  .contacts {
    position: absolute; left: 556px; top: 298px; list-style: none;
    font-family: "Lato", sans-serif; font-size: 25px; color: var(--text-soft);
  }
  .contacts li { display: flex; align-items: center; height: 37px; }
  .contacts svg { width: 28px; height: 28px; margin-right: 12px; flex: none; }
  .address-band {
    position: absolute; left: 0; right: 0; top: 455px; height: 62px;
    background: linear-gradient(90deg, var(--gold-deep), var(--gold-light) 50%, var(--gold-deep));
  }
  .address {
    position: absolute; right: 272px; top: 455px; height: 62px;
    display: flex; align-items: center;
    font-family: "Montserrat", sans-serif; font-size: 24px; color: var(--text-soft);
  }
</style>
</head>
<body>
  <main class="card">
    <div class="brand-name">VELTRA</div>
    <div class="tagline">Smarter Homes</div>

    <div class="person">
      <div class="person-name">Derek Halloran</div>
      <div class="person-role">Managing Director</div>
    </div>
    <div class="divider"></div>

    <ul class="contacts">
      <li>
        <svg viewBox="0 0 28 28" aria-hidden="true"><circle cx="14" cy="14" r="14" fill="var(--gold)"/><path d="M8 11c0-2 2-3 6-3s6 1 6 3l-2 1-1-2h-6l-1 2zM9 19l2-5h6l2 5z" fill="var(--card-dark)"/></svg>
        +34-602-518-794
      </li>
      <li>
        <svg viewBox="0 0 28 28" aria-hidden="true"><circle cx="14" cy="14" r="14" fill="var(--gold)"/><rect x="7" y="9" width="14" height="10" rx="1" fill="var(--card-dark)"/><path d="M7 10l7 5 7-5" stroke="var(--gold)" stroke-width="1.4" fill="none"/></svg>
        DHalloran@VELTRAsmarthomes.com
      </li>
      <li>
        <svg viewBox="0 0 28 28" aria-hidden="true"><circle cx="14" cy="14" r="14" fill="var(--gold)"/><circle cx="14" cy="14" r="7" fill="none" stroke="var(--card-dark)" stroke-width="1.6"/><path d="M7 14h14M14 7c-3 4-3 10 0 14M14 7c3 4 3 10 0 14" stroke="var(--card-dark)" stroke-width="1.4" fill="none"/></svg>
        www.VELTRAsmarthomes.com
      </li>
    </ul>

    <div class="address-band"></div>
    <div class="address">Plaza Brisa Local 42, Port Andratx, 07392</div>
  </main>
</body>
</html>
```